Love cats? Love the planet? We need a design for the most eco-friendly cat grass kit box ever!

We need a box designed for our new product - the world's most eco-friendly cat grass kit ever!

Text and documents attached. Text can be copied and pasted. It has been spell-checked already.

Some pictures need to be sourced and/or drawn.

It needs to be eye-catching in its simplicity and minimalism. Not too many colors, swirls, curlicues and stuff. Just simple. And the 'green' nature of it (biodegradability, 'save the planet', recycle, re-use, sustainable contents etc needs to be visible from a distance to stand out from the crowd).

Final design needs to communicate love of cats and the planet.

Target Market(s)

Apartment-dwelling cat owners

Industry/Entity Type

Pet Care

Font styles to use
Other font styles liked:
• Comfortaa

Colors

Designer to choose colors to be used in the design.

Requirements
Must have
• Clear, clean, simple and eye-catching design. Not overloaded with images and text. A cute cartoon/drawn cat munching on the cat grass.
• A drawn pot that heavily matches the actual pot in terms of color, shape and texture.

```html
<!DOCTYPE html>
<html lang="en">
<head>
<meta charset="utf-8">
<title>Cat Grass Kit – Box Panels</title>
<link rel="stylesheet" href="https://fonts.googleapis.com/css2?family=Fredoka:wght@600;700&family=Nunito:wght@700;800;900&family=Yanone+Kaffeesatz:wght@400;600&display=swap">
<style>
  :root {
    --backdrop: #c6c9d4;
    --panel-white: #f7f8f4;
    --leaf: #8dc63f;
    --leaf-light: #b5d96a;
    --meadow: #5fae3a;
    --meadow-deep: #2f8a3a;
    --moss: #3f7f34;
    --soil: #3a1f17;
    --tangerine: #f0a020;
    --tangerine-deep: #e2851a;
    --title-red: #e63a25;
    --sky-blue: #4aaad0;
    --ink-green: #5e9b2a;
    --pot-brown: #9b5a32;
  }
  * { box-sizing: border-box; margin: 0; padding: 0; }
  html, body { width: 1200px; height: 1200px; overflow: hidden; }
  body {
    background: var(--backdrop);
    font-family: "Nunito", sans-serif;
    position: relative;
  }

  .box-layout {
    position: absolute;
    left: 60px;
    top: 120px;
    display: grid;
    grid-template-columns: 640px 440px;
    grid-template-rows: 320px 640px;
  }
  .box-layout > section { box-shadow: 0 18px 40px rgba(40, 44, 60, 0.22); }

  /* ---------- Top panel ---------- */
  .top-panel {
    grid-column: 1;
    grid-row: 1;
    position: relative;
    background: linear-gradient(180deg, #9ccc3c 0%, var(--leaf) 100%);
    border-bottom: 2px solid #7cb236;
  }
  .top-disc {
    position: absolute;
    left: 210px;
    top: 50px;
    width: 220px;
    height: 220px;
    border-radius: 50%;
    background: radial-gradient(circle at 45% 40%, #6fb54a 0%, #4a9a3a 60%, #3f8a34 100%);
  }
  .top-title {
    position: absolute;
    left: 210px;
    top: 78px;
    width: 220px;
    text-align: center;
    font-family: "Fredoka", sans-serif;
    font-weight: 700;
    line-height: 0.95;
  }
  .top-title span { display: block; }
  .top-title .word-cat { color: var(--title-red); font-size: 56px; }
  .top-title .word-grass { color: var(--tangerine); font-size: 56px; }
  .top-title .word-kit { color: var(--tangerine-deep); font-size: 50px; }

  /* ---------- Front panel ---------- */
  .front-panel {
    grid-column: 1;
    grid-row: 2;
    position: relative;
    background: var(--panel-white);
    overflow: hidden;
  }
  .meadow {
    position: absolute;
    left: 0;
    top: 260px;
    width: 640px;
    height: 300px;
    background: linear-gradient(180deg, var(--leaf-light) 0%, var(--leaf) 22%, var(--meadow) 45%, var(--meadow-deep) 100%);
  }
  .brand {
    position: absolute;
    left: 34px;
    top: 40px;
    display: flex;
    align-items: center;
    gap: 10px;
  }
  .brand-dot {
    width: 18px; height: 18px;
    border-radius: 50%;
    background: var(--tangerine);
  }
  .brand-name {
    font-family: "Nunito", sans-serif;
    font-weight: 900;
    font-size: 30px;
    color: var(--tangerine-deep);
    letter-spacing: 0.5px;
  }

  .title-disc {
    position: absolute;
    left: 190px;
    top: 40px;
    width: 270px;
    height: 270px;
    border-radius: 50%;
    background: radial-gradient(circle at 45% 40%, #6fb54a 0%, #4a9a3a 60%, #3f8a34 100%);
  }
  .title {
    position: absolute;
    left: 190px;
    top: 62px;
    width: 270px;
    text-align: center;
    font-family: "Fredoka", sans-serif;
    font-weight: 700;
    line-height: 0.95;
  }
  .title span { display: block; }
  .title .word-cat { color: var(--title-red); font-size: 72px; }
  .title .word-grass { color: var(--tangerine); font-size: 72px; }
  .title .word-kit { color: var(--tangerine-deep); font-size: 64px; }

  .cert-seal {
    position: absolute;
    left: 488px;
    top: 84px;
    width: 116px;
    height: 116px;
    border-radius: 50%;
    background: var(--sky-blue);
    border: 6px solid #ffffff;
    box-shadow: 0 0 0 4px var(--sky-blue);
  }

  .claim-tags {
    position: absolute;
    left: 38px;
    top: 370px;
    display: flex;
    flex-direction: column;
    gap: 14px;
  }
  .claim-tag {
    width: 104px;
    padding: 6px 4px;
    border-radius: 12px;
    background: var(--tangerine);
    border: 2px solid #ffd27a;
    color: #ffffff;
    font-weight: 800;
    font-size: 19px;
    line-height: 1.02;
    text-align: center;
  }

  .cats-art {
    position: absolute;
    left: 318px;
    top: 330px;
    width: 300px;
    height: 220px;
    border-radius: 110px 110px 0 0;
    background: linear-gradient(160deg, #e9883f 0%, #d7d24a 45%, #f3f1ea 75%, #e3e3df 100%);
  }

  .slogan-band {
    position: absolute;
    left: 0;
    bottom: 0;
    width: 640px;
    height: 90px;
    background: var(--soil);
    display: flex;
    align-items: center;
    justify-content: center;
  }
  .slogan {
    font-family: "Nunito", sans-serif;
    font-weight: 800;
    font-size: 22px;
    color: #ffffff;
    letter-spacing: 1px;
  }

  /* ---------- Side panel ---------- */
  .side-panel {
    grid-column: 2;
    grid-row: 2;
    position: relative;
    background: var(--panel-white);
    border-left: 2px solid #e2e4de;
    overflow: hidden;
    font-family: "Yanone Kaffeesatz", sans-serif;
  }
  .side-brand {
    position: absolute;
    right: 26px;
    top: 30px;
    font-family: "Nunito", sans-serif;
    font-weight: 900;
    font-size: 18px;
    color: var(--tangerine-deep);
  }
  .side-title {
    position: absolute;
    left: 30px;
    top: 66px;
    font-weight: 600;
    font-size: 42px;
    color: var(--tangerine);
  }
  .contents {
    position: absolute;
    left: 30px;
    top: 124px;
    width: 250px;
    color: var(--ink-green);
    font-size: 19px;
    line-height: 1.2;
  }
  .eco-mark {
    position: absolute;
    right: 44px;
    top: 150px;
    width: 44px;
    height: 44px;
    border-radius: 50%;
    border: 4px solid var(--leaf);
  }
  .pot-photo {
    position: absolute;
    right: 26px;
    top: 232px;
    width: 120px;
    height: 190px;
    border-radius: 40px 40px 10px 10px;
    background: linear-gradient(180deg, #7fc24a 0%, #4e9a33 55%, var(--pot-brown) 56%, #6d3c22 100%);
  }
  .warning {
    position: absolute;
    left: 30px;
    top: 400px;
    width: 260px;
  }
  .warning-label {
    display: inline-block;
    background: var(--ink-green);
    color: #ffffff;
    font-weight: 600;
    font-size: 20px;
    letter-spacing: 1px;
    padding: 2px 10px;
    margin-bottom: 6px;
  }
  .warning-text {
    color: var(--ink-green);
    font-size: 19px;
    line-height: 1.2;
  }
  .side-grass {
    position: absolute;
    left: 0;
    bottom: 0;
    width: 440px;
    height: 120px;
    background: linear-gradient(180deg, rgba(141,198,63,0) 0%, var(--leaf-light) 55%, var(--leaf) 100%);
  }
  .website {
    position: absolute;
    left: 30px;
    bottom: 16px;
    font-size: 18px;
    color: var(--moss);
  }
</style>
</head>
<body>
  <main class="box-layout">
    <section class="top-panel">
      <div class="top-disc" role="img" aria-label="Painted green grass circle behind the lid title"></div>
      <p class="top-title">
        <span class="word-cat">CAT</span>
        <span class="word-grass">GRASS</span>
        <span class="word-kit">KIT</span>
      </p>
    </section>

    <section class="front-panel">
      <div class="meadow" role="img" aria-label="Rolling green hills and tall grass meadow"></div>

      <div class="brand">
        <span class="brand-dot"></span>
        <span class="brand-name">Purrnest</span>
      </div>

      <div class="title-disc" role="img" aria-label="Painted green grass circle behind the title"></div>
      <h1 class="title">
        <span class="word-cat">CAT</span>
        <span class="word-grass">GRASS</span>
        <span class="word-kit">KIT</span>
      </h1>

      <div class="cert-seal" role="img" aria-label="Organic certification seal"></div>

      <div class="claim-tags">
        <p class="claim-tag">USA<br>grown</p>
        <p class="claim-tag">100%<br>non-gmo</p>
      </div>

      <div class="cats-art" role="img" aria-label="Illustration of four cartoon cats peeking over the grass"></div>

      <div class="slogan-band">
        <p class="slogan">THE GREENEST CAT GRASS KIT...EVER. SERIOUSLY</p>
      </div>
    </section>

    <section class="side-panel">
      <p class="side-brand">Purrnest</p>
      <h2 class="side-title">CAT GRASS KIT</h2>
      <p class="contents">
        100% non-gmo, organic, USA-grown:<br>
        rye (secale cereale) 1oz<br>
        oat (avena sativa) 1oz<br>
        barley (hordeum vulgare) 1oz<br>
        wheat (triticum aestivum) 1oz seeds<br>
        organic coconut coir growing mix 1oz<br>
        Sprouts in 3 to 5 days. Sprinkle, water, wait, then let kitty graze.
      </p>
      <div class="eco-mark" role="img" aria-label="Recyclable packaging mark"></div>
      <div class="pot-photo" role="img" aria-label="Photo of fresh cat grass growing in a brown fibre pot"></div>
      <div class="warning">
        <span class="warning-label">WARNING</span>
        <p class="warning-text">Only for cats. Not for human consumption. Keep out of reach of children.</p>
      </div>
      <div class="side-grass" role="img" aria-label="Soft green grass edge"></div>
      <p class="website">www.purrnest-kits.com</p>
    </section>
  </main>
</body>
</html>
```